Mexican Restaurant needs a new Menu Design

Mexican restaurant LAS TORTUGAS is renewing its menu, so we need something new.
Since our inception we have given the task of rescuing ingredients, recipes, and traditional and representatives dishes of the culinary techniques of yesteryear.
We are the only restaurant in Guadalajara that manufactures its own dairy natural as fresh cheese, the cream and our already well-known and traditional jocoqui. In addition, we produce organic ranch egg and are currently in the development of organic vegetables cultivated on the slopes of the old Hill which gives our plants benefit from an exceptional microclimate.
Find more information about the restaurant in www.lastortugasfonda.example.
The menu needs to have the full list of products with the prices, some phrases that speak of the philosophy of the ranch-style-living, photos.
We need the cover, back cover and interiors.
Updates
Thank you so much for the proposals you have submitted for the menu design. We are looking them carefully.
Thank you very much for taking your time to design a proposal for our menu!!!
Target Market(s)
The target is very wide (28-40 yrs.): Young executives, Young families, Housewives.
Industry/Entity Type
Restaurant
Look and feel
Each slider illustrates characteristics of the customer's brand and the style your logo design should communicate.

```html
<!DOCTYPE html>
<html lang="en">
<head>
<meta charset="utf-8">
<title>Las Tortugas – Dinner Menu</title>
<link rel="stylesheet" href="https://fonts.googleapis.com/css2?family=Bebas+Neue&family=Crimson+Text:wght@400&family=Oswald:wght@300;400&display=swap">
<style>
  :root {
    --backdrop: #e9e6e1;
    --cover-red: #d9484b;
    --cover-red-deep: #c83a3e;
    --paper: #ffffff;
    --ink: #3a3a3a;
    --ink-soft: #5a5a5a;
    --accent: #e26a6a;
    --accent-line: #f1b7b4;
    --heading-grey: #9a9a9a;
  }
  * { box-sizing: border-box; margin: 0; padding: 0; }
  html, body { width: 1200px; height: 900px; overflow: hidden; }
  body {
    background: var(--backdrop);
    position: relative;
    font-family: "Crimson Text", Georgia, serif;
    color: var(--ink);
  }

  /* Cover */
  .cover {
    position: absolute; left: 40px; top: 40px;
    width: 540px; height: 820px;
    background: radial-gradient(ellipse at 40% 35%, var(--cover-red) 0%, var(--cover-red-deep) 100%);
    box-shadow: 0 6px 18px rgba(0,0,0,.25);
    text-align: center;
    color: #fff;
  }
  .cover-title {
    position: absolute; top: 470px; left: 0; right: 0;
    font-family: "Bebas Neue", "Oswald", sans-serif;
    font-size: 54px; letter-spacing: 2px;
  }
  .cover-subtitle {
    position: absolute; top: 560px; left: 0; right: 0;
    font-family: "Oswald", sans-serif; font-weight: 300;
    font-size: 34px; letter-spacing: 12px; color: #4a4a4a;
  }
  .cover-year {
    position: absolute; top: 735px; left: 0; right: 0;
    font-size: 20px; letter-spacing: 2px;
  }
  .cover-address {
    position: absolute; top: 770px; left: 0; right: 0;
    font-size: 15px; letter-spacing: 1px;
  }

  /* Inner page */
  .menu-page {
    position: absolute; left: 620px; top: 40px;
    width: 540px; height: 820px;
    background: var(--paper);
    box-shadow: 0 6px 18px rgba(0,0,0,.25);
    padding: 34px 40px 0;
    text-align: center;
  }
  .brand {
    font-family: "Bebas Neue", sans-serif;
    font-size: 24px; letter-spacing: 1px; color: var(--accent);
  }
  .menu-title {
    margin-top: 26px;
    font-family: "Oswald", sans-serif; font-weight: 400;
    font-size: 26px; letter-spacing: 8px; color: var(--ink);
  }
  .double-rule { height: 5px; border-top: 1px solid var(--accent-line); border-bottom: 1px solid var(--accent-line); margin: 12px 0 0; }
  .divider-mark { color: var(--accent); font-size: 16px; letter-spacing: 3px; margin-top: 8px; }
  .section-title {
    font-family: "Bebas Neue", sans-serif;
    font-size: 30px; letter-spacing: 6px; color: var(--heading-grey);
    margin-top: 16px;
  }
  .dish-name {
    font-family: "Bebas Neue", sans-serif;
    font-size: 17px; letter-spacing: .3px; color: var(--ink); line-height: 1;
  }
  .dish-desc { font-size: 13px; color: var(--ink-soft); line-height: 1.15; }
  .dish { margin-top: 8px; }
  .dish-list-wide .dish { margin-top: 10px; }
  .two-columns {
    display: grid; grid-template-columns: 1fr 1fr; gap: 0 20px; margin-top: 6px;
  }
  .main-courses { position: relative; margin-top: 4px; padding: 6px 10px 14px; }
  .bracket { position: absolute; inset: 0; width: 100%; height: 100%; }
</style>
</head>
<body>

<section class="cover">
  <h1 class="cover-title">Las Tortugas</h1>
  <p class="cover-subtitle">~ MENU ~</p>
  <p class="cover-year">2013</p>
  <p class="cover-address">Av. del Roble # 415, Col. Las Lomas, Zapopan, Jalisco</p>
</section>

<section class="menu-page">
  <p class="brand">Las Tortugas</p>
  <h2 class="menu-title">DINNER MENU</h2>
  <div class="double-rule"></div>
  <p class="divider-mark">···//···</p>

  <h3 class="section-title">STARTERS &amp; SALADS</h3>
  <div class="double-rule" style="margin-top:4px"></div>

  <div class="dish-list-wide">
    <div class="dish">
      <p class="dish-name">Country style spreads with salad and guacamole</p>
      <p class="dish-desc">walnuts, cheese, walnuts, cheese, walnuts, cheese, w/ walnuts, cheese &amp; walnuts, cheese</p>
    </div>
    <div class="dish">
      <p class="dish-name">Country style spreads</p>
      <p class="dish-desc">walnuts, cheese, walnuts, cheese, walnuts, cheese, w/ walnuts, cheese &amp; walnuts, cheese</p>
    </div>
  </div>

  <div class="two-columns">
    <div>
      <div class="dish"><p class="dish-name">Picante plate</p><p class="dish-desc">picante bread, chilli, meat &amp; armadillo</p></div>
      <div class="dish"><p class="dish-name">Picante plate</p><p class="dish-desc">picante bread, chilli, meat &amp; armadillo</p></div>
      <div class="dish"><p class="dish-name">Taco loco</p><p class="dish-desc">picante bread, chilli,</p></div>
      <div class="dish"><p class="dish-name">Picante plate</p><p class="dish-desc">picante bread, chilli, meat &amp; armadillo</p></div>
    </div>
    <div>
      <div class="dish"><p class="dish-name">Picante plate</p><p class="dish-desc">picante bread, chilli, meat &amp; armadillo</p></div>
      <div class="dish"><p class="dish-name">Picante plate and taco</p><p class="dish-desc">picante bread, chilli, meat &amp; armadillo</p></div>
      <div class="dish"><p class="dish-name">Picante plate</p><p class="dish-desc">picante bread, chilli, meat &amp; armadillo</p></div>
      <div class="dish"><p class="dish-name">Picante plate, funghi e prosciutto</p><p class="dish-desc">picante bread, chilli, meat &amp; armadillo</p></div>
    </div>
  </div>

  <div class="double-rule" style="margin-top:12px"></div>
  <h3 class="section-title">MAIN COURSES</h3>

  <div class="main-courses dish-list-wide">
    <svg class="bracket" viewBox="0 0 460 250" preserveAspectRatio="none" aria-hidden="true">
      <g fill="none" stroke="#f1b7b4" stroke-width="1">
        <polyline points="0,250 0,40 20,40 20,10 200,10"/>
        <polyline points="6,250 6,46 26,46 26,16 200,16"/>
        <polyline points="460,0 460,210 440,210 440,240 260,240"/>
        <polyline points="454,0 454,204 434,204 434,234 260,234"/>
      </g>
    </svg>
    <div class="dish"><p class="dish-name">Country style spreads</p><p class="dish-desc">walnuts, cheese, walnuts, cheese, walnuts, cheese, w/ walnuts, cheese &amp; walnuts, cheese</p></div>
    <div class="dish"><p class="dish-name">Country style spreads</p><p class="dish-desc">walnuts, cheese, walnuts, cheese, walnuts, cheese, w/ walnuts, cheese &amp; walnuts, cheese</p></div>
    <div class="dish"><p class="dish-name">Traditional style soups for vegetarians</p><p class="dish-desc">walnuts, cheese, walnuts, cheese, walnuts, cheese, w/ walnuts, cheese &amp; walnuts, cheese</p></div>
    <div class="dish"><p class="dish-name">Country spreads</p><p class="dish-desc">walnuts, cheese, walnuts, cheese, walnuts, cheese, w/ walnuts, cheese &amp; walnuts, cheese</p></div>
  </div>
  <div class="double-rule" style="margin-top:6px"></div>
</section>

</body>
</html>
```